Organization for CEO's Needs New Rebranding Concept

(Please note: we are NOT looking for a logo design, just a concept design to create the brand(colours,designs) around our existing logo)
Our organization Velmora Leaders Circle (www.velmoraleaderscircle.org) is in the process of rebranding in all aspects including our website, imagery, and slogan.
We are looking for a concept that will encapsulate this rebranding/change in the form of an image that can then be adapted almost everywhere (website, presentations, posters etc).
Our new slogan is “The house of collective wisdom, and future thinking. A seal of leadership and positive impact.” Ideally, we would like this new concept to express this slogan (“house” is used metaphorically, we do not want it literally in the image).
Ultimately, we want the concept to express the elements of an ecosystem/community of CEO’s and entrepreneurs who have a powerful voice on leadership and move together to co-create value for themselves, their organizations and society for the future. It would help for the image to not be too complicated for it to adapt to various formats, dimensions and situations.
You can view our website to understand our identity and attempt to create a new brand for our organization that is more modern.
Target Market(s)
Our audience are CEO's and entrepreneurs in an exclusive community
Look and feel
Each slider illustrates characteristics of the customer's brand and the style your logo design should communicate.

```html
<!DOCTYPE html>
<html lang="en">
<head>
<meta charset="utf-8">
<title>Velmora Leaders Circle — The House of Collective Wisdom</title>
<link rel="stylesheet" href="https://fonts.googleapis.com/css2?family=Poppins:wght@500;700;800&display=swap">
<style>
  :root {
    --ink: #111111;
    --paper: #ffffff;
    --teal: #2b7f98;
    --teal-deep: #1f5f78;
    --peach: #f2c9a0;
    --amber: #e8a777;
    --rose: #c9798f;
    --violet: #8a5ea8;
  }
  * { margin: 0; padding: 0; box-sizing: border-box; }
  html, body {
    width: 1200px; height: 655px; overflow: hidden;
    background: var(--paper);
  }
  .banner {
    position: relative;
    width: 1200px; height: 655px;
    overflow: hidden;
    font-family: "Poppins", sans-serif;
    color: var(--paper);
  }
  .banner__photo {
    position: absolute; inset: 0;
    background:
      radial-gradient(ellipse 420px 520px at 760px 330px, rgba(246,226,210,0.55), transparent 70%),
      radial-gradient(ellipse 360px 460px at 1040px 430px, rgba(200,170,205,0.6), transparent 70%),
      linear-gradient(180deg, rgba(255,255,255,0) 60%, rgba(120,80,150,0.35) 100%),
      linear-gradient(90deg, var(--teal-deep) 0%, var(--teal) 14%, #8aa6a8 30%, var(--peach) 45%, var(--amber) 62%, var(--rose) 82%, var(--violet) 100%);
  }
  .banner__tint {
    position: absolute; inset: 0;
    background: linear-gradient(180deg, rgba(255,190,140,0.10) 0%, rgba(150,100,190,0.35) 100%);
  }
  .headline { position: absolute; left: 0; top: 0; width: 100%; height: 100%; }
  .headline__line {
    position: absolute; left: 104px;
    white-space: nowrap; letter-spacing: -1px;
  }
  .headline__lead  { top: 176px; font-weight: 800; font-size: 58px; line-height: 60px; }
  .headline__key   { top: 250px; font-weight: 800; font-size: 86px; line-height: 76px; }
  .headline__word  { top: 326px; font-weight: 800; font-size: 86px; line-height: 76px; }
  .headline__sub   { top: 396px; font-weight: 700; font-size: 63px; line-height: 72px; letter-spacing: -1.5px; }
  .headline__tag {
    top: 476px; left: 106px;
    background: var(--paper); color: var(--ink);
    padding: 0 10px 0 8px;
    font-weight: 500; font-size: 24px; line-height: 31px; letter-spacing: 0;
  }
</style>
</head>
<body>
  <main class="banner">
    <div class="banner__photo" role="img" aria-label="Photograph of two businesswomen in conversation on a sofa in a bright modern office, one holding a clipboard"></div>
    <div class="banner__tint"></div>

    <h1 class="headline">
      <span class="headline__line headline__lead">THE HOUSE OF</span>
      <span class="headline__line headline__key">COLLECTIVE</span>
      <span class="headline__line headline__word">WISDOM</span>
      <span class="headline__line headline__sub">and future thinking</span>
      <span class="headline__line headline__tag">A seal of leadership and positive impact</span>
    </h1>
  </main>
</body>
</html>
```